Halvorine.com Web Banner Design

Halvorine.com is a national online business magazine that helps people in Canada start and grow their business. We have over 2000 articles, ask-the-expert answers and guides, as well as a free business directory.

We want to expand awareness for our site and need an exciting, promotional leaderboard and bigbox ad that is highly successful in getting people to click to visit our site, so the ads need to effectively create a sense of urgency. The two ads should share a consistent design and message.

The theme for this first ad group should be that anyone starting a business in Canada should come to Halvorine for the answers they need to succeed. We are looking for creativity and the ads also need to be consistent with the Halvorine brand.
Updates

Reason: Posting on the weekend seems to have limited the number of responses. We do design in house and are outsourcing this project because of time constraints - but we are looking for agency quality work. Check out examples from leading design blogs of great banner ad designs to get a feel for the quality we are looking for. Thank you!

Reason: Liking several of the designs and now just waiting for feedback from some of our advisors!

Reason: Still waiting for input, thank you for your patience. Also, for submissions that have a big box only, we are going to need to have a leaderboard version of the final design.

Target Market(s)

Canadians who or either starting a business or are running their own company with up to 25 staff. Some will be entrepreneurs with plans to grow to be a big company, others will want to make a living and don't want to grow. The common need is that they feel an urgency to get help and to get answers that will let them run their business effectively.

Requirements
Must have
• Halvorine.com name, clearly branded
• Halvorine logo (can be ad the end of the rotation of the ad)
• File size must be 150 kb or smaller
• Leaderboard size: 728 x90 pixels
• Big Box size: 250 x 250 pixels

```html
<!DOCTYPE html>
<html lang="en">
<head>
<meta charset="utf-8">
<title>Halvorine.com Big Box Banners</title>
<link rel="stylesheet" href="https://fonts.googleapis.com/css2?family=Arimo:wght@400;700&display=swap">
<style>
  :root {
    --stage: #332f2f;
    --paper: #ffffff;
    --brand-red: #dd0b37;
    --ink: #3a3a3c;
    --logo-grey: #5b5b5e;
    --swoosh: #7d7d80;
    --frame: #cfcfcf;
  }
  * { box-sizing: border-box; margin: 0; padding: 0; }
  html, body {
    width: 1200px; height: 900px; overflow: hidden;
    background: var(--stage);
    font-family: "Arimo", Arial, sans-serif;
  }
  .banner {
    position: absolute; top: 264px;
    width: 372px; height: 372px;
    background: var(--paper);
    border: 1px solid var(--frame);
    overflow: hidden;
  }
  .banner--help { left: 190px; }
  .banner--info { left: 633px; }

  .photo {
    position: absolute; left: 0; top: 0; width: 100%; height: 300px;
  }
  .banner--help .photo {
    background: linear-gradient(160deg, #cfe3ea 0%, #9fbccb 35%, #e8eef2 60%, #c8a48c 80%, #b9cfe0 100%);
  }
  .banner--info .photo {
    background: linear-gradient(180deg, #f4f6f7 0%, #e6ebee 45%, #d9ccc0 70%, #eef0f1 100%);
  }
  .footer-wave {
    position: absolute; left: 0; top: 250px; width: 100%; height: 122px;
  }
  .headline {
    position: absolute; left: 21px; top: 16px;
    color: var(--ink); font-size: 30px; line-height: 38px; font-weight: 400;
  }
  .headline__accent {
    display: block; color: var(--brand-red); font-weight: 700;
    font-size: 40px; line-height: 46px; letter-spacing: -0.5px;
    text-shadow: 0 0 6px #ffffff, 0 0 3px #ffffff;
  }
  .banner--info .headline { left: 22px; top: 12px; line-height: 39px; }
  .cta {
    position: absolute; left: 20px; top: 104px;
    width: 138px; height: 46px; border-radius: 3px;
    background: var(--brand-red); color: #fff;
    font-weight: 700; font-size: 24px; line-height: 46px; text-align: center;
  }
  .logo {
    position: absolute; left: 0; right: 0; top: 312px;
    text-align: center;
    font-size: 30px; font-weight: 400; letter-spacing: 5px;
    color: var(--logo-grey);
  }
</style>
</head>
<body>

<section class="banner banner--help">
  <div class="photo" role="img" aria-label="Photo of two business people shaking hands"></div>
  <svg class="footer-wave" viewBox="0 0 372 122" preserveAspectRatio="none" aria-hidden="true">
    <path d="M0 26 C120 8 260 10 372 26 L372 122 L0 122 Z" fill="#ffffff"/>
    <path d="M0 26 C120 8 260 10 372 26 C260 18 120 18 0 34 Z" fill="var(--swoosh)"/>
  </svg>
  <h2 class="headline"><span class="headline__accent">Get FREE help</span>starting your<br>business</h2>
  <div class="logo">HALVORINE</div>
</section>

<section class="banner banner--info">
  <div class="photo" role="img" aria-label="Photo of three colleagues smiling around a tablet in a bright office"></div>
  <svg class="footer-wave" viewBox="0 0 372 122" preserveAspectRatio="none" aria-hidden="true">
    <path d="M0 26 C120 8 260 10 372 26 L372 122 L0 122 Z" fill="#ffffff"/>
    <path d="M0 26 C120 8 260 10 372 26 C260 18 120 18 0 34 Z" fill="var(--swoosh)"/>
  </svg>
  <h2 class="headline">Get the information<br>you need to succeed</h2>
  <div class="cta">Visit now</div>
  <div class="logo">HALVORINE</div>
</section>

</body>
</html>
```